Investment Advisor E-Newsletter Banner Design

I need a banner designed for an email newsletter that will be sent monthly to clients and prospects. We want to see designs that are elegant and use our logo well. The banner should be 922x150px and should go well with the www.bhtlwest.com website. Should include Logo and email and phone number.

Target Market(s)

High net worth investors

Number of Pages Required

1 page

Requirements
Must have
• logo, place for email (info@bhtlwest.com) and phone number (555-219-0387), colors and design that work well with www.bhtlwest.com website

```html
<!DOCTYPE html>
<html lang="en">
<head>
<meta charset="utf-8">
<title>Bluehill Trust West – Newsletter Banners</title>
<link href="https://fonts.googleapis.com/css2?family=Lato:ital,wght@0,700;0,900;1,900&family=Gentium+Book+Plus&display=swap" rel="stylesheet">
<style>
  :root {
    --backdrop: #efb273;
    --paper: #ffffff;
    --brand-navy: #2f2f86;
    --curve-blue: #4645c0;
    --contact-purple: #5855a6;
    --night: #060d18;
    --coins-light: #e9e3da;
    --coins-mid: #8a7e72;
    --dusk-light: #7d826f;
    --dusk-dark: #565e52;
    --white: #ffffff;
  }
  * { margin: 0; padding: 0; box-sizing: border-box; }
  html, body { width: 1200px; height: 943px; overflow: hidden; background: var(--backdrop); }
  .sheet {
    position: absolute; left: 0; top: 0;
    width: 1072px; height: 842px;
    transform: scale(1.1194); transform-origin: 0 0;
  }
  .banner {
    position: absolute; left: 87px;
    width: 922px; height: 150px; overflow: hidden;
    font-family: "Lato", sans-serif;
  }
  .banner--one { top: 85px; }
  .banner--two { top: 266px; }
  .banner--three { top: 448px; }
  .banner--four { top: 629px; }

  .banner__photo { position: absolute; inset: 0; }
  .banner__photo--coins {
    background: linear-gradient(90deg, var(--coins-light) 22%, var(--coins-mid) 45%, #2a2a30 58%, var(--night) 70%);
  }
  .banner__photo--walker {
    background: linear-gradient(90deg, var(--dusk-light) 25%, var(--dusk-dark) 50%, #6a7060 100%);
  }

  .banner__brand-panel { position: absolute; left: 0; top: 0; width: 250px; height: 150px; }

  .brand {
    position: absolute; left: 14px; top: 52px;
    display: flex; align-items: center; gap: 10px;
  }
  .brand__dot { width: 34px; height: 34px; border-radius: 50%; background: var(--brand-navy); }
  .brand__name {
    font-family: "Gentium Book Plus", serif; color: var(--brand-navy);
    font-size: 17px; line-height: 1.15;
  }
  .banner__count {
    position: absolute; left: 14px; top: 126px;
    font-size: 12px; font-weight: 700; color: var(--brand-navy);
  }

  .banner__headline {
    position: absolute; left: 610px; top: 14px;
    color: var(--white); font-weight: 900; font-style: italic;
    font-size: 37px; line-height: 36px; letter-spacing: 0.3px;
  }

  .contact-bar { position: absolute; left: 500px; top: 102px; width: 422px; height: 48px; }
  .contact-bar__shape { position: absolute; inset: 0; }
  .contact-bar__items {
    position: absolute; left: 24px; top: 0; height: 48px;
    display: flex; align-items: center; gap: 22px;
    color: var(--white); font-weight: 700; font-size: 18px;
  }
  .contact-item { display: flex; align-items: center; gap: 10px; }
  .contact-item svg { display: block; }
</style>
</head>
<body>
<main class="sheet">

  <!-- Banner variants -->
  <section class="banner banner--one">
    <div class="banner__photo banner__photo--coins" role="img" aria-label="Photo of a hand stacking coins beside a rising arrow"></div>
    <svg class="banner__brand-panel" viewBox="0 0 250 150" aria-hidden="true">
      <path d="M0 0 H203 Q255 75 203 150 H0 Z" fill="var(--paper)"/>
      <path d="M203 0 Q255 75 203 150" fill="none" stroke="var(--curve-blue)" stroke-width="4"/>
    </svg>
    <div class="brand"><span class="brand__dot"></span><span class="brand__name">Bluehill Trust West<br>Advisory, Inc.</span></div>
    <span class="banner__count">x10</span>
    <h1 class="banner__headline">Evidence-Based<br>Investing</h1>
    <div class="contact-bar">
      <svg class="contact-bar__shape" viewBox="0 0 422 48" preserveAspectRatio="none" aria-hidden="true"><path d="M18 0 H422 V48 H0 Z" fill="var(--contact-purple)"/></svg>
      <div class="contact-bar__items">
        <span class="contact-item"><svg width="16" height="16" viewBox="0 0 24 24"><path fill="#fff" d="M6.6 10.8a15.1 15.1 0 0 0 6.6 6.6l2.2-2.2c.3-.3.7-.4 1-.2 1.1.4 2.3.6 3.6.6.6 0 1 .4 1 1V20c0 .6-.4 1-1 1A17 17 0 0 1 3 4c0-.6.4-1 1-1h3.5c.6 0 1 .4 1 1 0 1.3.2 2.5.6 3.6.1.3 0 .7-.2 1z"/></svg>555-219-0387</span>
        <span class="contact-item"><svg width="19" height="15" viewBox="0 0 24 18"><path fill="#fff" d="M0 2a2 2 0 0 1 2-2h20a2 2 0 0 1 2 2v.5L12 10 0 2.5zM0 5l12 7.5L24 5v11a2 2 0 0 1-2 2H2a2 2 0 0 1-2-2z"/></svg>info@bhtlwest.com</span>
      </div>
    </div>
  </section>

  <section class="banner banner--two">
    <div class="banner__photo banner__photo--coins" role="img" aria-label="Photo of a hand stacking coins beside a rising arrow"></div>
    <svg class="banner__brand-panel" viewBox="0 0 250 150" aria-hidden="true">
      <path d="M0 0 H203 Q255 75 203 150 H0 Z" fill="var(--paper)"/>
      <path d="M203 0 Q255 75 203 150" fill="none" stroke="var(--curve-blue)" stroke-width="4"/>
    </svg>
    <div class="brand"><span class="brand__dot"></span><span class="brand__name">Bluehill Trust West<br>Advisory, Inc.</span></div>
    <span class="banner__count">x10</span>
    <div class="contact-bar">
      <svg class="contact-bar__shape" viewBox="0 0 422 48" preserveAspectRatio="none" aria-hidden="true"><path d="M18 0 H422 V48 H0 Z" fill="var(--contact-purple)"/></svg>
      <div class="contact-bar__items">
        <span class="contact-item"><svg width="16" height="16" viewBox="0 0 24 24"><path fill="#fff" d="M6.6 10.8a15.1 15.1 0 0 0 6.6 6.6l2.2-2.2c.3-.3.7-.4 1-.2 1.1.4 2.3.6 3.6.6.6 0 1 .4 1 1V20c0 .6-.4 1-1 1A17 17 0 0 1 3 4c0-.6.4-1 1-1h3.5c.6 0 1 .4 1 1 0 1.3.2 2.5.6 3.6.1.3 0 .7-.2 1z"/></svg>555-219-0387</span>
        <span class="contact-item"><svg width="19" height="15" viewBox="0 0 24 18"><path fill="#fff" d="M0 2a2 2 0 0 1 2-2h20a2 2 0 0 1 2 2v.5L12 10 0 2.5zM0 5l12 7.5L24 5v11a2 2 0 0 1-2 2H2a2 2 0 0 1-2-2z"/></svg>info@bhtlwest.com</span>
      </div>
    </div>
  </section>

  <section class="banner banner--three">
    <div class="banner__photo banner__photo--walker" role="img" aria-label="Photo of a businessman seen from behind, jacket over shoulder, facing a dusk sky"></div>
    <svg class="banner__brand-panel" viewBox="0 0 250 150" aria-hidden="true">
      <path d="M0 0 H203 Q255 75 203 150 H0 Z" fill="var(--paper)"/>
      <path d="M203 0 Q255 75 203 150" fill="none" stroke="var(--curve-blue)" stroke-width="4"/>
    </svg>
    <div class="brand"><span class="brand__dot"></span><span class="brand__name">Bluehill Trust West<br>Advisory, Inc.</span></div>
    <span class="banner__count">x10</span>
    <h1 class="banner__headline">Evidence-Based<br>Investing</h1>
    <div class="contact-bar">
      <svg class="contact-bar__shape" viewBox="0 0 422 48" preserveAspectRatio="none" aria-hidden="true"><path d="M18 0 H422 V48 H0 Z" fill="var(--contact-purple)"/></svg>
      <div class="contact-bar__items">
        <span class="contact-item"><svg width="16" height="16" viewBox="0 0 24 24"><path fill="#fff" d="M6.6 10.8a15.1 15.1 0 0 0 6.6 6.6l2.2-2.2c.3-.3.7-.4 1-.2 1.1.4 2.3.6 3.6.6.6 0 1 .4 1 1V20c0 .6-.4 1-1 1A17 17 0 0 1 3 4c0-.6.4-1 1-1h3.5c.6 0 1 .4 1 1 0 1.3.2 2.5.6 3.6.1.3 0 .7-.2 1z"/></svg>555-219-0387</span>
        <span class="contact-item"><svg width="19" height="15" viewBox="0 0 24 18"><path fill="#fff" d="M0 2a2 2 0 0 1 2-2h20a2 2 0 0 1 2 2v.5L12 10 0 2.5zM0 5l12 7.5L24 5v11a2 2 0 0 1-2 2H2a2 2 0 0 1-2-2z"/></svg>info@bhtlwest.com</span>
      </div>
    </div>
  </section>

  <section class="banner banner--four">
    <div class="banner__photo banner__photo--walker" role="img" aria-label="Photo of a businessman seen from behind, jacket over shoulder, facing a dusk sky"></div>
    <svg class="banner__brand-panel" viewBox="0 0 250 150" aria-hidden="true">
      <path d="M0 0 H203 Q255 75 203 150 H0 Z" fill="var(--paper)"/>
      <path d="M203 0 Q255 75 203 150" fill="none" stroke="var(--curve-blue)" stroke-width="4"/>
    </svg>
    <div class="brand"><span class="brand__dot"></span><span class="brand__name">Bluehill Trust West<br>Advisory, Inc.</span></div>
    <span class="banner__count">x10</span>
    <div class="contact-bar">
      <svg class="contact-bar__shape" viewBox="0 0 422 48" preserveAspectRatio="none" aria-hidden="true"><path d="M18 0 H422 V48 H0 Z" fill="var(--contact-purple)"/></svg>
      <div class="contact-bar__items">
        <span class="contact-item"><svg width="16" height="16" viewBox="0 0 24 24"><path fill="#fff" d="M6.6 10.8a15.1 15.1 0 0 0 6.6 6.6l2.2-2.2c.3-.3.7-.4 1-.2 1.1.4 2.3.6 3.6.6.6 0 1 .4 1 1V20c0 .6-.4 1-1 1A17 17 0 0 1 3 4c0-.6.4-1 1-1h3.5c.6 0 1 .4 1 1 0 1.3.2 2.5.6 3.6.1.3 0 .7-.2 1z"/></svg>555-219-0387</span>
        <span class="contact-item"><svg width="19" height="15" viewBox="0 0 24 18"><path fill="#fff" d="M0 2a2 2 0 0 1 2-2h20a2 2 0 0 1 2 2v.5L12 10 0 2.5zM0 5l12 7.5L24 5v11a2 2 0 0 1-2 2H2a2 2 0 0 1-2-2z"/></svg>info@bhtlwest.com</span>
      </div>
    </div>
  </section>

</main>
</body>
</html>
```